Business Cards for a Junk Removal Company

Hello,
We are looking to have business cards designed that are simple, bold, easy to read, and right to the point. Please see the attachments for our logo files. We want the card to be yellow on both sides ( Color code Yellow: #FFE01B). The logo text font is (Rockstar Extra Bold) and this is also in the files attached. Please make the text black for the logo. On the back side of the card, you can use white and black for text. Thank you in advance for your hard work!

Front of card-
Harbor Haul Removal (logo)
Back of card-
Harbor Haul Removal
Donate - Recycle - Dispose
518-276-9053
www.harborhaulremoval.example
info@harborhaulremoval.example

Industry/Entity Type

Junk removal

Contact Information for Business Card

FRONT OF CARD- Harbor Haul Removal (logo) BACK OF CARD- Harbor Haul Removal Donate - Recycle - Dispose 518-276-9053 www.harborhaulremoval.example info@harborhaulremoval.example

Font styles to use
Other font styles liked:
• Rockstar Extra Bold

Colors
FFF300
FFF600
FEFA6F
FFFEC7
FFFEE8

Requirements
Must have
• Must have color code Yellow: #FFE01B for the background of front and back of the card

```html
<!DOCTYPE html>
<html lang="en">
<head>
<meta charset="utf-8">
<title>Harbor Haul Removal — Business Cards</title>
<link href="https://fonts.googleapis.com/css2?family=Archivo+Black&family=Montserrat:wght@400&display=swap" rel="stylesheet">
<style>
  :root {
    --card-yellow: #FFE01B;
    --ink: #000000;
    --backdrop: #dcdcda;
  }
  * { margin: 0; padding: 0; box-sizing: border-box; }
  html, body {
    width: 1200px;
    height: 801px;
    overflow: hidden;
    background: var(--backdrop);
  }
  .sheet {
    position: relative;
    width: 1200px;
    height: 801px;
  }
  .card {
    position: absolute;
    top: 252px;
    width: 520px;
    height: 297px;
    background: var(--card-yellow);
    color: var(--ink);
  }
  .card--back { left: 60px; }
  .card--front { left: 620px; }

  .brand-name {
    font-family: "Archivo Black", sans-serif;
    font-weight: 400;
    text-transform: uppercase;
    color: var(--ink);
    line-height: 1.05;
    text-align: center;
  }

  /* Back side */
  .back-logo {
    position: absolute;
    left: 0;
    top: 0;
    width: 215px;
    height: 297px;
    display: flex;
    align-items: center;
    justify-content: center;
    font-size: 21px;
  }
  .divider {
    position: absolute;
    left: 215px;
    top: 62px;
    width: 1.5px;
    height: 173px;
    background: var(--ink);
  }
  .details {
    position: absolute;
    left: 236px;
    top: 72px;
    right: 16px;
  }
  .details__name {
    font-family: "Archivo Black", sans-serif;
    font-size: 15px;
    text-transform: uppercase;
    letter-spacing: 0.2px;
  }
  .details__tagline {
    font-family: "Montserrat", sans-serif;
    font-size: 13px;
    margin-top: 3px;
  }
  .contact-list {
    list-style: none;
    margin-top: 26px;
  }
  .contact-list li {
    display: flex;
    align-items: center;
    gap: 8px;
    font-family: "Montserrat", sans-serif;
    font-size: 11.5px;
    margin-bottom: 7px;
  }
  .contact-list svg {
    width: 12px;
    height: 12px;
    flex: none;
  }

  /* Front side */
  .front-logo {
    position: absolute;
    inset: 0;
    display: flex;
    align-items: center;
    justify-content: center;
    font-size: 48px;
  }
</style>
</head>
<body>
<main class="sheet">

  <section class="card card--back" aria-label="Business card, back">
    <div class="back-logo">
      <p class="brand-name">Harbor Haul<br>Removal</p>
    </div>
    <div class="divider"></div>
    <div class="details">
      <h2 class="details__name">Harbor Haul Removal</h2>
      <p class="details__tagline">Donate - Recycle - Dispose</p>
      <ul class="contact-list">
        <li>
          <svg viewBox="0 0 12 12" aria-hidden="true"><path fill="#000" d="M2.4 0.6 4 2.6 3.1 4a6.4 6.4 0 0 0 4.9 4.9l1.4-0.9 2 1.6-1 2C5.4 11.4 0.6 6.6 0.4 1.6z"/></svg>
          518-276-9053
        </li>
        <li>
          <svg viewBox="0 0 12 12" aria-hidden="true"><rect x="0.5" y="2" width="11" height="8" fill="#000"/><path d="M0.8 2.4 6 6.6l5.2-4.2" stroke="#FFE01B" stroke-width="1" fill="none"/></svg>
          info@harborhaulremoval.example
        </li>
        <li>
          <svg viewBox="0 0 12 12" aria-hidden="true"><circle cx="6" cy="6" r="5.5" fill="#000"/><path d="M0.8 6h10.4M6 0.6c-2.4 2.8-2.4 8 0 10.8M6 0.6c2.4 2.8 2.4 8 0 10.8" stroke="#FFE01B" stroke-width="0.8" fill="none"/></svg>
          www.harborhaulremoval.example
        </li>
      </ul>
    </div>
  </section>

  <section class="card card--front" aria-label="Business card, front">
    <div class="front-logo">
      <p class="brand-name">Harbor Haul<br>Removal</p>
    </div>
  </section>

</main>
</body>
</html>
```